Fence Flyer to Attract More Sales During Winter

We need a new flyer made that we can distribute to residential mailboxes. The flyer is to promote our Frostline Picket Days. We like simply designs, and we would like the flyer to showcase a lot of our fence photos. More of our photos are online at our website at www.getbramblerail.com - our new address needs to also be featured on the flyer - 436 Quillen rd, Monroe, NC 28117. I do want the words "FROSTLINE PICKET DAYS" to be dominate on the flyer with the description "Wood fences starting at $12/FT!" Please look through our Facebook page and our website to gather more photos or information. We are flexible on colors, nothing to fancy - simple flyer design please.

Target Market(s)

Residential homeowners that need a new fence to enclose their yard for safety, security or decorative

Industry/Entity Type

Residential Construction

Font styles to use
Sans Serif

Colors

Designer to choose colors to be used in the design.

Requirements
Must have
• Frostline Picket Days
• Contact information for the business
• "Come visit our outdoor showroom, open 24/7!"
Nice to have
• Photos of our fences - you can find more on our website at www.GetBrambleRail.com or Facebook.com/MeadowlarkRailGPV
Should not have
• Flashy designs

```html
<!DOCTYPE html>
<html lang="en">
<head>
<meta charset="utf-8">
<title>Frostline Picket Days Flyer</title>
<link href="https://fonts.googleapis.com/css2?family=Montserrat:wght@400;500;600;800&display=swap" rel="stylesheet">
<style>
:root{
  --stage:#d3d3d3;
  --paper:#ffffff;
  --ink:#1f1f1f;
  --charcoal:#262626;
  --gold:#8a6d2f;
  --orange:#e08a1e;
  --brand-blue:#2a7fc8;
  --muted:#555555;
}
*{box-sizing:border-box;margin:0;padding:0}
html,body{width:1200px;height:844px;overflow:hidden}
body{background:var(--stage);font-family:"Montserrat",Arial,sans-serif;color:var(--ink);position:relative}
.flyer{position:absolute;left:317px;top:22px;width:566px;height:800px;background:var(--paper);overflow:hidden;box-shadow:0 6px 18px rgba(0,0,0,.18)}
.block{position:absolute}
.photo{position:absolute}
.hero-photo{left:0;top:0;width:566px;height:335px;
  clip-path:polygon(240px 0,566px 0,566px 335px,0 335px,0 100px,175px 100px);
  background:linear-gradient(180deg,#6f9bd6 0%,#a9c3e6 38%,#b98a62 55%,#e5d3a2 72%,#d9c38d 100%)}
.brand{position:absolute;left:20px;top:26px;display:flex;align-items:center;gap:10px}
.brand-mark{width:34px;height:34px;background:var(--gold)}
.brand-name{font-weight:600;font-size:17px;color:var(--brand-blue);line-height:1}
.brand-phone{font-weight:800;font-size:15px;color:var(--ink);line-height:1.2}
.brand-tagline{font-size:6.5px;color:var(--ink);font-style:normal}
.offer{left:325px;top:250px;width:241px;height:95px;background:var(--gold);
  clip-path:polygon(40px 0,100% 0,100% 100%,0 100%);color:#fff;text-align:right;padding:14px 18px 0 0}
.offer-line{font-size:18px;font-weight:500;line-height:1.1}
.offer-price{font-size:26px;font-weight:800}
.offer-price small{font-size:15px;font-weight:500}
.headline-panel{left:0;top:300px;width:305px;height:225px;background:var(--charcoal);
  clip-path:polygon(0 0,270px 0,305px 35px,305px 100%,0 100%);padding:30px 0 0 24px}
.headline{font-weight:800;font-size:47px;line-height:.98;color:#fff;letter-spacing:-.5px}
.headline .accent{color:var(--orange);display:block}
.photo-row-a{top:345px;height:110px}
.photo-a1{left:310px;width:118px;background:linear-gradient(160deg,#4d7a3c,#8a7554 55%,#c96a6a)}
.photo-a2{left:433px;width:133px;background:linear-gradient(160deg,#b7c6cf,#a88a66 55%,#6e5a3f)}
.showroom{left:230px;top:460px;width:336px;height:180px;background:var(--charcoal);padding:90px 0 0 22px;color:#fff}
.showroom p{font-size:20px;font-weight:500;line-height:1.12}
.showroom .open{color:var(--orange)}
.photo-b1{left:0;top:530px;width:225px;height:110px;background:linear-gradient(160deg,#3f6b2f,#6d8a3f 45%,#d9c38d)}
.contact{left:0;top:650px;width:566px;height:85px;display:flex;align-items:center;padding:0 22px}
.call{display:flex;align-items:center;gap:10px;padding-right:20px;border-right:1px solid #999}
.call-label{font-size:8px;font-weight:500;letter-spacing:.3px}
.call-number{font-size:25px;font-weight:800;line-height:1}
.details{padding-left:18px;list-style:none;font-size:10px;color:var(--muted)}
.details li{display:flex;align-items:center;gap:7px;line-height:1.7}
.footer{left:0;top:740px;width:566px;height:60px;background:var(--gold);display:flex;align-items:center;justify-content:flex-end;gap:8px;padding-right:22px;color:#fff;font-size:11px}
.social-square{width:20px;height:20px;background:#fff}
</style>
</head>
<body>
<main class="flyer">
  <div class="photo hero-photo" role="img" aria-label="Photo of a new wooden privacy fence in front of a red brick house under a blue sky"></div>

  <header class="brand">
    <div class="brand-mark"></div>
    <div>
      <div class="brand-name">Bramble Rail Fence</div>
      <div class="brand-phone">704-555-0142</div>
      <div class="brand-tagline">"Because Good Fences Make Good Neighbors"</div>
    </div>
  </header>

  <div class="block offer">
    <div class="offer-line">Wood fences</div>
    <div class="offer-price"><small>starting at </small>$12/FT!</div>
  </div>

  <section class="block headline-panel">
    <h1 class="headline">FROSTLINE<span class="accent">PICKET</span>DAYS</h1>
  </section>

  <div class="photo photo-row-a photo-a1" role="img" aria-label="Photo of a wooden fence along a garden with roses"></div>
  <div class="photo photo-row-a photo-a2" role="img" aria-label="Photo of a wooden fence gate with dark hardware"></div>

  <section class="block showroom">
    <p>Come visit our<br>outdoor showroom<br><span class="open">Open 24/7!</span></p>
  </section>

  <div class="photo photo-b1" role="img" aria-label="Photo of a scalloped picket fence beside green shrubs"></div>

  <section class="block contact">
    <div class="call">
      <svg width="30" height="30" viewBox="0 0 30 30" fill="none" stroke="#8a6d2f" stroke-width="2">
        <path d="M8 4c-2 0-4 2-3 5 2 7 7 12 14 14 3 1 5-1 5-3l-4-4-3 2c-3-1-6-4-7-7l2-3z"/>
      </svg>
      <div>
        <div class="call-label">CALL FOR AN APPOINTMENT</div>
        <div class="call-number">704-555-0142</div>
      </div>
    </div>
    <ul class="details">
      <li><svg width="10" height="12" viewBox="0 0 10 12"><path d="M5 0a4 4 0 0 0-4 4c0 3 4 8 4 8s4-5 4-8a4 4 0 0 0-4-4z" fill="#8a6d2f"/><circle cx="5" cy="4" r="1.5" fill="#fff"/></svg>436 Quillen rd, Monroe, NC 28117</li>
      <li><svg width="12" height="9" viewBox="0 0 12 9"><rect width="12" height="9" fill="#8a6d2f"/><path d="M0 0l6 5 6-5" stroke="#fff" fill="none"/></svg>office@getbramblerail.com</li>
      <li><svg width="12" height="10" viewBox="0 0 12 10" fill="none" stroke="#8a6d2f" stroke-width="1.4"><rect x="1" y="1" width="10" height="6"/><path d="M4 9h4"/></svg>www.getbramblerail.com</li>
    </ul>
  </section>

  <footer class="block footer">
    <span>Follow us on</span>
    <span class="social-square"></span>
    <span class="social-square"></span>
  </footer>
</main>
</body>
</html>
```